Tarno Booking website (www.tarnobooking.example)

My company develops booking software, Tarno Booking, for the hourly booking of resources such as classes in a school or customer booking involving rooms in a spa. These bookings also involve the customers, staff, rooms and a lesson or treatment.

The main difference between this software and general calendar software such as Zindle calendar is that this Tarno Booking allows resources such as people and rooms to be associated with the bookings. This is important for example in the case of a Spa to make sure the rooms are booked appropriately and to see the free times for the rooms. For a golf practice range the players much be booked to the tee spots where they practice golf.

I have tried to design the website myself, as a computer programmer- I am a bit "square" and not a designer, my first attempt is http://www.tarnobooking.example/, my second attempt is at http://www.pelumwerks.example/tarnobookingwebsite/
I am not happy with my designs as compared to the professional designs I see people can come up with here. The software must have the image of a professional software product in order to inspire the confidence of customers.

Am looking for a design which will be the most likely to give the customer the following feeling:
* Confident the product can do the job.
* Feel easy to want to try it, at least for the free trial.
* Its a professional software product and also a web based product, the user can login from the web.

Look at other booking software websites for ideas, here is a list of links to similar booking products. These products all have different features but are mostly for resource booking.
http://pelumwerks.example/tarnobookingwebsite/?page=compare
Updates

Hello all,

Thankyou for the designs so far, to save peoples time, I will try to eliminate the bottom 50% of designs now.

To be honest, most of the designs are of a good or high quality, I think its very tough on you as graphic and web designers. Only a minor few are of low quality.

If your design is discarded - I would say its unlikely that you are going to be able to produce a design that will beat the competition. 
You probably already know, you could try to re-sell your design later for other projects or as a template on one of those template websites. Some of these discarded designs are quite worthwhile designs.

Best regards, Gareth

Target Market(s)

Spa, Gym, School, Golf, any organization who manages bookings of their customers

Industry/Entity Type

Software

Requirements
Must have
• Home page and inner page, any other pages up to you.

Make a logo or use the image of the girl that I already have on the second design.

Menu(s) for navigation.

A language switcher for 3 languages, English, Chinese Traditional and Chinese Simplified. (Western, Hong Kong and Chinese mainland market are important).

Space for a video introduction, it could be small and when the user clicks on it then it gets bigger then it won't take up too much space. Up to you.

A space for the user to login and register a new account.

Screenshots.

I don't have any strong preferences, use your own ideas, if you look at all the other products you can get the basic idea from them.

The total goal is to make a website which is going to lead to sales of the software product.

```html
<!DOCTYPE html>
<html lang="en">
<head>
<meta charset="utf-8">
<title>Tarno Booking – Advanced Booking System</title>
<link rel="stylesheet" href="https://fonts.googleapis.com/css2?family=Arimo:ital,wght@0,400;0,700;1,700&family=Tinos&family=Ubuntu:wght@500&display=swap">
<style>
:root{
  --dark:#1f1f1f;
  --dark2:#2b2b2b;
  --orange:#e8731a;
  --orange-light:#f39a3c;
  --blue:#1f5fa8;
  --text:#555;
  --light:#f0f0f0;
  --line:#d6d6d6;
  --white:#fff;
}
*{box-sizing:border-box;margin:0;padding:0}
html,body{width:911px;height:1200px;overflow:hidden;background:var(--white)}
body{font-family:"Arimo",Arial,sans-serif;color:var(--text);font-size:9.5px;position:relative}
.abs{position:absolute}
a{color:inherit;text-decoration:none}

.site-header{left:0;top:0;width:911px;height:113px;background:linear-gradient(#2e2e2e,#161616)}
.top-bar{left:515px;top:0;width:318px;height:22px;background:#3a3a3a;border-radius:0 0 6px 6px;color:#ddd;font-size:8px;display:flex;align-items:center;gap:9px;padding-left:16px}
.top-bar .join{color:#5ab0f0;font-weight:700}
.top-bar .lang::after{content:" ▾";color:var(--orange)}
.brand{left:77px;top:24px;display:flex;align-items:center;gap:7px}
.brand-mark{width:26px;height:26px;background:var(--orange);border-radius:3px}
.brand-name{font-family:"Ubuntu",sans-serif;font-size:29px;color:var(--white);line-height:1}
.brand-tag{left:132px;top:54px;font-size:10px;color:#ddd}

.main-nav{left:76px;top:87px;width:759px;height:24px;background:linear-gradient(#4a4a4a,#2a2a2a);border-radius:3px;display:flex;align-items:center;font-size:11px;color:#eee}
.main-nav a{padding:0 12px;height:24px;line-height:24px;border-right:1px solid #555}
.main-nav a.active{background:var(--orange);color:var(--white)}
.search{left:610px;top:89px;width:218px;height:20px;display:flex}
.search .field{flex:1;background:var(--white);border-radius:10px 0 0 10px;font-size:9px;color:#999;line-height:20px;padding-left:22px}
.search .go{width:30px;background:var(--orange);color:var(--white);font-weight:700;font-size:11px;text-align:center;line-height:20px;border-radius:0 10px 10px 0}
.sub-nav{left:0;top:113px;width:911px;height:24px;background:var(--orange);color:var(--white);font-size:10.5px;display:flex;gap:24px;padding-left:88px;line-height:24px}

.slider{left:76px;top:168px;width:759px;height:275px;background:#333;border-radius:4px;box-shadow:0 14px 22px rgba(0,0,0,.25)}
.slide-tab{top:11px;width:38px;height:250px;background:linear-gradient(90deg,#2a2a2a,#3b3b3b);border-radius:3px}
.slide-tab .label{position:absolute;left:11px;top:72px;transform:rotate(-90deg);transform-origin:left top;color:#ddd;font-size:11px;white-space:nowrap}
.slide-tab .num{position:absolute;bottom:10px;width:100%;text-align:center;color:#222;font-size:18px;font-weight:700}
.slide-panel{left:179px;top:11px;width:571px;height:250px;border-radius:2px;overflow:hidden;background:linear-gradient(135deg,#ffd71c,#f9a20c 55%,#f07e14)}
.slide-panel .base{position:absolute;left:0;bottom:0;width:100%;height:70px}
.calendar-art{left:48px;top:34px;width:172px;height:150px;border-radius:6px;background:linear-gradient(#f08a2a 0 25%,#f4f4f4 25%)}
.offer{left:263px;top:42px;color:var(--white);font-style:italic;font-weight:700;font-size:60px;line-height:1;white-space:nowrap}
.offer small{font-size:22px}
.offer-points{left:263px;top:117px;color:var(--white);font-size:12px;font-weight:700;line-height:17px}
.btn{top:183px;height:36px;line-height:36px;color:var(--white);font-style:italic;font-weight:700;font-size:18px;padding-left:14px;clip-path:polygon(0 0,88% 0,100% 50%,88% 100%,0 100%)}
.btn-buy{left:262px;width:142px;background:linear-gradient(#2d8ed1,#125a98)}
.btn-trial{left:422px;width:120px;background:linear-gradient(#a8a8a8,#707070)}

.intro-video{left:76px;top:480px;width:154px;height:103px;background:linear-gradient(135deg,#3c4a52,#1b2126)}
.intro-video .play{position:absolute;left:60px;top:35px;width:32px;height:32px;border-radius:50%;border:2px solid #ccc;background:rgba(255,255,255,.15)}
.intro-video .play::after{content:"";position:absolute;left:11px;top:8px;border-left:11px solid #ddd;border-top:7px solid transparent;border-bottom:7px solid transparent}
.intro h2{font-size:12.5px;font-weight:400;color:var(--blue);margin-bottom:6px}
.intro{left:246px;top:482px;width:328px;line-height:13.7px}
.intro .link{color:var(--blue)}
.intro-more{left:76px;top:596px;width:500px;line-height:13.7px}

.news{left:601px;top:480px;width:234px;height:150px;border:1px solid var(--line);border-radius:4px}
.news h3{height:25px;line-height:25px;background:#f3f3f3;border-bottom:1px solid var(--line);padding-left:9px;font-size:8.5px;color:#333}
.news-item{padding:0 8px;margin-top:11px;font-size:8.5px;line-height:13.5px}
.news-item p{color:var(--blue)}
.news .more{position:absolute;right:8px;bottom:5px;font-size:8px;color:var(--blue)}

.features-head{left:76px;top:657px;width:759px;height:36px;background:linear-gradient(#5a5a5a,#3a3a3a);color:var(--white);font-weight:700;font-size:13.5px;line-height:36px;padding-left:13px}
.features{left:76px;top:693px;width:759px;height:137px;background:linear-gradient(#e4e4e4,#fafafa)}
.feature{top:21px;width:133px;height:98px;overflow:hidden;border:2px solid var(--white)}
.feature .art{height:100%}
.feature .cap{position:absolute;left:0;bottom:0;width:100%;height:38px;background:rgba(243,140,55,.85);color:var(--white);font-size:11.5px;display:flex;align-items:center;justify-content:center;text-align:center;line-height:12px}

.suit h2,.clients h2{font-family:"Tinos",serif;font-weight:400;font-size:16.5px}
.suit{left:76px;top:852px;width:342px}
.suit h2{color:#555}
.suit .lead{font-size:9px;color:#222;margin:6px 0 10px}
.suit li{list-style:none;height:18.2px;line-height:18.2px;background:var(--light);border-bottom:1px solid var(--white);color:var(--blue);font-size:9.2px;padding-left:24px;position:relative}
.suit li::before{content:"";position:absolute;left:10px;top:6px;width:5px;height:5px;border-right:2px solid var(--blue);border-top:2px solid var(--blue);transform:rotate(45deg)}

.clients{left:453px;top:852px}
.clients h2{color:var(--blue)}
.client{width:58px;border:2px solid var(--orange)}
.shot-a{height:58px;background:linear-gradient(#f5f5f5 0 30%,#e9e4dc 30%)}
.shot-b{height:54px;background:linear-gradient(#d9c3e6 0 30%,#a9d8a0 30%)}

.site-footer{left:0;top:1049px;width:911px;height:151px;background:var(--dark2);color:#aaa;font-size:8.3px}
.site-footer .divider{position:absolute;left:259px;top:0;width:1px;height:151px;background:#444}
.foot-links{line-height:15.3px}
.site-footer h4{color:var(--white);font-size:9.5px}
.contact{line-height:13.7px}
.site-footer .accent{color:var(--orange)}
.social{width:24px;height:24px;border-radius:4px}
</style>
</head>
<body>

<header class="site-header abs">
  <div class="top-bar abs"><span class="lang">LANGUAGES</span><span>WELCOME MIRELA TOSK</span><span>LOGOUT</span><span class="join">JOIN NOW</span></div>
  <div class="brand abs"><span class="brand-mark"></span><span class="brand-name">TarnoBooking</span></div>
  <div class="brand-tag abs">Advanced Booking System</div>
  <nav class="main-nav abs">
    <a>About Tarno Booking</a><a class="active">Videos</a><a>Documentation</a><a>Free Trial</a><a>Purchase</a><a style="border:0">Compare</a>
  </nav>
  <div class="search abs"><div class="field">Type Keyword</div><div class="go">GO</div></div>
</header>
<nav class="sub-nav abs"><a>Booking Management Videos</a><a>Customer Videos</a><a>Staff Videos</a></nav>

<section class="slider abs">
  <div class="slide-tab abs" style="left:11px"><span class="label">Slide One</span><span class="num">1</span></div>
  <div class="slide-tab abs" style="left:53px"><span class="label">Slide Two</span><span class="num">2</span></div>
  <div class="slide-tab abs" style="left:95px"><span class="label">Slide Three</span><span class="num">3</span></div>
  <div class="slide-tab abs" style="left:137px"><span class="label">Slide Four</span><span class="num">4</span></div>
  <div class="slide-panel abs">
    <svg class="base" viewBox="0 0 571 70" preserveAspectRatio="none"><path d="M0 30 Q280 -10 571 22 L571 70 L0 70Z" fill="#fff"/><path d="M0 30 Q280 -10 571 22" stroke="#d9751a" stroke-width="3" fill="none"/></svg>
    <div class="calendar-art abs" role="img" aria-label="Illustration of a January desk calendar"></div>
    <div class="offer abs">Get 35<small>%OFF</small></div>
    <div class="offer-points abs">» The Best Way for Booking with Ease<br>» Full Featured 30-Day Trial</div>
    <a class="btn btn-buy abs">BUY TODAY!</a>
    <a class="btn btn-trial abs">FREE TRIAL</a>
  </div>
</section>

<div class="intro-video abs" role="img" aria-label="Introduction video still"><span class="play"></span></div>
<section class="intro abs">
  <h2>Tarno Booking Introduction</h2>
  <p>Tarno Booking is front office booking software which makes managing bookings, room and staff availability fast and simple.</p>
  <p>We focus on producing quality software which is powerful yet easy to use. This is suitable for many types of business, <span class="link">click here to view all the available business types and to learn more about how this software can help you directly.</span></p>
</section>
<p class="intro-more abs">Tarno Booking stores all data on our servers in the SaaS model giving a very low total cost of ownership our customers. You have zero investment in server platform hardware, zero investment in software licenses, zero investment in hardware and software upgrades, as these are included as part of the service.</p>

<aside class="news abs">
  <h3>LATEST NEWS</h3>
  <div class="news-item"><span>18 OCT 2011</span><p>Lorem ipsum dolor sit amet commodo porttitor, felis. Nam blandit</p></div>
  <div class="news-item"><span>18 OCT 2011</span><p>Lorem ipsum dolor sit amet commodo porttitor, felis. Nam blandit</p></div>
  <a class="more">More News ›</a>
</aside>

<div class="features-head abs">FEATURE SPOTLIGHTS</div>
<section class="features abs">
  <div class="feature abs" style="left:11px"><div class="art" role="img" aria-label="Cloud server diagram" style="background:linear-gradient(#f4f4f4,#bfe1f2)"></div><div class="cap">CLOUD HOSTED</div></div>
  <div class="feature abs" style="left:160px"><div class="art" role="img" aria-label="Operating system platforms illustration" style="background:linear-gradient(#f6f6f6,#ddd)"></div><div class="cap">MULTI PLATFORM</div></div>
  <div class="feature abs" style="left:308px"><div class="art" role="img" aria-label="Colourful rising bars illustration" style="background:linear-gradient(90deg,#e05a2a,#2d9ee0,#7cc23b)"></div><div class="cap">INCREASED<br>PRODUCTIVITY</div></div>
  <div class="feature abs" style="left:458px"><div class="art" role="img" aria-label="Illustration of staff members" style="background:linear-gradient(#f1f1f1,#d9a35a)"></div><div class="cap">MULTIPLE STAFF<br>MEMBERS</div></div>
  <div class="feature abs" style="left:606px"><div class="art" role="img" aria-label="Stopwatch illustration" style="background:radial-gradient(circle at 50% 40%,#fff,#bbb)"></div><div class="cap">VARIABLE MINUTE<br>INTERVALS</div></div>
</section>

<section class="suit abs">
  <h2>Is Tarno Booking suitable for my business?</h2>
  <p class="lead">Tarno Booking works well for the following types of businesses :</p>
  <ul>
    <li>Spa, Gym, Weight Management Center or types of businesses</li>
    <li>Golf Practice range with many tees for golfers to practice golf</li>
    <li>Room bookings such as meeting rooms, library rooms, computer rooms</li>
    <li>Conference of meeting booings</li>
    <li>Language teaching school, Music school, Educational center</li>
    <li>Schools which consults to schools by sending teachers to those schools</li>
  </ul>
</section>

<section class="clients abs">
  <h2>Our Clients</h2>
  <div class="client abs" style="left:0;top:28px"><div class="shot-a" role="img" aria-label="Client website screenshot"></div></div>
  <div class="client abs" style="left:65px;top:28px"><div class="shot-a" role="img" aria-label="Client website screenshot"></div></div>
  <div class="client abs" style="left:130px;top:28px"><div class="shot-a" role="img" aria-label="Client website screenshot"></div></div>
  <div class="client abs" style="left:195px;top:28px"><div class="shot-a" role="img" aria-label="Client website screenshot"></div></div>
  <div class="client abs" style="left:260px;top:28px"><div class="shot-a" role="img" aria-label="Client website screenshot"></div></div>
  <div class="client abs" style="left:325px;top:28px"><div class="shot-a" role="img" aria-label="Client website screenshot"></div></div>
  <div class="client abs" style="left:0;top:94px"><div class="shot-b" role="img" aria-label="Client website screenshot"></div></div>
  <div class="client abs" style="left:65px;top:94px"><div class="shot-b" role="img" aria-label="Client website screenshot"></div></div>
  <div class="client abs" style="left:130px;top:94px"><div class="shot-b" role="img" aria-label="Client website screenshot"></div></div>
  <div class="client abs" style="left:195px;top:94px"><div class="shot-b" role="img" aria-label="Client website screenshot"></div></div>
  <div class="client abs" style="left:260px;top:94px"><div class="shot-b" role="img" aria-label="Client website screenshot"></div></div>
  <div class="client abs" style="left:325px;top:94px"><div class="shot-b" role="img" aria-label="Client website screenshot"></div></div>
</section>

<footer class="site-footer abs">
  <div class="divider"></div>
  <div class="foot-links abs" style="left:89px;top:15px">About Us<br>Events<br>Press<br>Jobs<br>Resources<br>Staff</div>
  <div class="foot-links abs" style="left:168px;top:15px">Customer<br>Service<br>Contact Us<br>Privacy<br>Terms Of Use<br>Site Map<br>Website Feedback</div>
  <h4 class="abs" style="left:281px;top:19px">Contact Details</h4>
  <div class="contact abs" style="left:281px;top:48px">Pelumwerks Studio<br>Room 412, Harlow Court 3<br>18 Fenway Road, Westmere<br>Northbay, Eastland<br><br><span class="accent">www.tarnobooking.example</span></div>
  <div class="contact abs" style="left:432px;top:48px">Tel: (000) 555 01234<br>Fax 0000 555 019<br>Office Hours: 9:00am - 5:30pm<br><br><span class="accent">hello@pelumwerks.example</span></div>
  <div class="abs" style="right:77px;top:20px">Copyright © 2011 <span class="accent">TarnoBooking</span>. All rights reserved.</div>
  <h4 class="abs" style="right:77px;top:43px">Connect with Us</h4>
  <span class="social abs" style="left:771px;top:68px;background:#3b5a9a"></span>
  <span class="social abs" style="left:803px;top:68px;background:#3aaee0"></span>
</footer>

</body>
</html>
```